Logo & Visitenkarte für Hochzeitsplanerin
Zielgruppe
Mein Name ist Carola Wendt und ich bin Hochzeitsplanerin mit BVR Zertigfikat. Ich komme aus Köln und möchte als selbstständige Hochzeitsplanerin vor allem kölsche Hochzeiten und Hochzeiten mit Lumora Elementen anbieten. Meine Zielgruppe sind junge Brautpaare bis mitte/ende 30 welche genauso heimatverbunden sind wie ich.
Aufgabenstellung
Die Farben rosa und Bordeaux sollen vorkommen und es sollte ein wenig verspielt sein, jedoch nicht zu kindisch. Bitte auf der Visitenkarte noch Hochzeitsplanerin Carola Wendt (BVR) abbilden.

```html
<!DOCTYPE html>
<html lang="de">
<head>
<meta charset="utf-8">
<title>Ewig wir – Hochzeitsplanung Visitenkarte</title>
<link rel="stylesheet" href="https://fonts.googleapis.com/css2?family=Alex+Brush&family=Cormorant+SC:wght@500&display=swap">
<style>
  :root {
    --paper: #ffffff;
    --bordeaux: #5e1a1c;
    --rose: #e8b49c;
    --band: rgba(255, 255, 255, 0.72);
    --bloom-light: #f6e6e2;
    --bloom-pink: #e4b9b4;
    --bloom-red: #9c3a44;
    --bloom-deep: #5c2a33;
    --leaf: #6e8664;
    --leaf-soft: #a9b9a0;
  }
  * { margin: 0; padding: 0; box-sizing: border-box; }
  html, body {
    width: 1200px;
    height: 786px;
    overflow: hidden;
    background: var(--paper);
  }
  .card {
    position: relative;
    width: 1200px;
    height: 786px;
    background: var(--paper);
  }
  .bouquet-photo {
    position: absolute;
    left: 43px;
    top: 43px;
    width: 1114px;
    height: 700px;
    background:
      radial-gradient(ellipse 30% 22% at 48% 12%, rgba(246,230,226,0.95) 0%, rgba(246,230,226,0) 100%),
      radial-gradient(ellipse 22% 18% at 55% 90%, rgba(156,58,68,0.85) 0%, rgba(156,58,68,0) 100%),
      radial-gradient(ellipse 20% 25% at 88% 85%, rgba(110,134,100,0.9) 0%, rgba(110,134,100,0) 100%),
      radial-gradient(ellipse 20% 25% at 10% 88%, rgba(110,134,100,0.8) 0%, rgba(110,134,100,0) 100%),
      radial-gradient(ellipse 60% 55% at 50% 45%, var(--bloom-light) 0%, var(--bloom-pink) 45%, #c98a8c 75%, rgba(201,138,140,0) 100%),
      linear-gradient(135deg, var(--leaf-soft) 0%, var(--bloom-deep) 40%, var(--bloom-red) 60%, var(--leaf) 100%);
  }
  .brand-band {
    position: absolute;
    left: 43px;
    top: 194px;
    width: 1114px;
    height: 400px;
    background: var(--band);
  }
  .brand {
    position: absolute;
    left: 0;
    top: 194px;
    width: 1200px;
    height: 400px;
    display: flex;
    flex-direction: column;
    align-items: center;
    color: var(--bordeaux);
  }
  .brand-mark {
    margin-top: 44px;
    width: 150px;
    height: 150px;
  }
  .brand-name {
    margin-top: 26px;
    font-family: "Alex Brush", cursive;
    font-size: 80px;
    line-height: 1;
    font-weight: 400;
  }
  .brand-tagline {
    margin-top: 12px;
    display: flex;
    align-items: center;
    gap: 30px;
    font-family: "Cormorant SC", serif;
    font-weight: 500;
    font-size: 36px;
    letter-spacing: 1px;
    line-height: 1;
  }
  .heart {
    width: 24px;
    height: 22px;
    fill: var(--rose);
  }
</style>
</head>
<body>
  <main class="card">
    <div class="bouquet-photo" role="img" aria-label="Foto eines Brautstraußes mit roten Dahlien, hellrosa Rosen, Beeren und grünen Blättern"></div>
    <div class="brand-band"></div>
    <section class="brand">
      <svg class="brand-mark" viewBox="0 0 150 150" aria-hidden="true">
        <circle cx="75" cy="75" r="70" fill="none" stroke="var(--bordeaux)" stroke-width="4"/>
      </svg>
      <h1 class="brand-name">Ewig wir</h1>
      <p class="brand-tagline">
        <svg class="heart" viewBox="0 0 24 22" aria-hidden="true"><path d="M12 21 C5 15 0 11 0 6 A6 6 0 0 1 12 4 A6 6 0 0 1 24 6 C24 11 19 15 12 21 Z"/></svg>
        <span>Hochzeitsplanung</span>
        <svg class="heart" viewBox="0 0 24 22" aria-hidden="true"><path d="M12 21 C5 15 0 11 0 6 A6 6 0 0 1 12 4 A6 6 0 0 1 24 6 C24 11 19 15 12 21 Z"/></svg>
      </p>
    </section>
  </main>
</body>
</html>
```